Meridale painting

We are a Painting company. We paint residential and commercial, interior& exterior painting, cabinets refinish,acoustic ceiling painting,popcorn ceiling removal,drywall repair,iron and concrete painting

We don't have any Facebook page or website.

We are a Painting company. We paint residential and commercial, interior& exterior painting, cabinets refinish,acoustic ceiling painting,popcorn ceiling removal,drywall repair,iron and concrete painting We don't have any Facebook page or website.

Requirements
Must have
• I need 200 cards. 50 of with my name Tobin, 50 with Owen 50 with Harold qnd 50 with bastian

```html
<!DOCTYPE html>
<html lang="en">
<head>
<meta charset="utf-8">
<title>Meridale Painting — Business Cards</title>
<link rel="stylesheet" href="https://fonts.googleapis.com/css2?family=Cinzel:wght@400;500&family=Jost:wght@400&family=Source+Sans+3:wght@400&display=swap">
<style>
  :root {
    --backdrop: #1d1d1e;
    --card-light: #e7e7e7;
    --ink: #141414;
    --paper-white: #ffffff;
    --paint-red: #8e1f1c;
    --paint-orange: #b5521e;
    --paint-gold: #b8862a;
    --paint-blue: #1c4f8c;
    --paint-magenta: #7d1f6a;
    --paint-navy: #1a2450;
  }
  * { margin: 0; padding: 0; box-sizing: border-box; }
  html, body {
    width: 1093px; height: 1200px; overflow: hidden;
    background: var(--backdrop);
  }
  .canvas { position: relative; width: 1093px; height: 1200px; }

  .card {
    position: absolute;
    left: 264px;
    width: 580px;
    height: 357px;
    box-shadow: 0 3px 8px rgba(0,0,0,0.6);
    overflow: hidden;
  }

  /* Front card */
  .card-front { top: 226px; background: var(--card-light); color: var(--ink); text-align: center; }
  .brand-name {
    position: absolute; top: 46px; left: 0; width: 100%;
    font-family: "Cinzel", serif; font-weight: 400;
    font-size: 46px; letter-spacing: 0.3em; padding-left: 0.3em; line-height: 1;
  }
  .brand-sub {
    position: absolute; top: 99px; left: 0; width: 100%;
    display: flex; align-items: center; justify-content: center; gap: 12px;
  }
  .brand-sub .rule { width: 58px; height: 1.5px; background: var(--ink); }
  .brand-sub .word {
    font-family: "Jost", sans-serif; font-size: 20px;
    letter-spacing: 0.85em; padding-left: 0.85em; line-height: 1;
  }
  .holder-name {
    position: absolute; top: 170px; left: 0; width: 100%;
    font-family: "Cinzel", serif; font-size: 27px; line-height: 1; letter-spacing: 0.02em;
  }
  .holder-role {
    position: absolute; top: 197px; left: 0; width: 100%;
    font-family: "Source Sans 3", sans-serif; font-size: 16px; line-height: 1;
  }
  .holder-divider {
    position: absolute; top: 228px; left: 218px; width: 143px; height: 1.5px; background: var(--ink);
  }
  .contact-list {
    position: absolute; top: 241px; left: 0; width: 100%;
    list-style: none;
    font-family: "Source Sans 3", sans-serif; font-size: 16px; line-height: 21px;
  }

  /* Back card */
  .card-back { top: 620px; color: var(--paper-white); text-align: center; }
  .paint-field {
    position: absolute; inset: 0;
    background:
      radial-gradient(ellipse at 18% 20%, var(--paint-red) 0%, transparent 45%),
      radial-gradient(ellipse at 55% 15%, var(--paint-gold) 0%, transparent 40%),
      radial-gradient(ellipse at 88% 30%, var(--paint-orange) 0%, transparent 45%),
      radial-gradient(ellipse at 15% 75%, var(--paint-blue) 0%, transparent 45%),
      radial-gradient(ellipse at 45% 88%, var(--paint-magenta) 0%, transparent 40%),
      radial-gradient(ellipse at 80% 80%, var(--paint-blue) 0%, transparent 45%),
      var(--paint-navy);
    filter: brightness(0.78);
  }
  .back-title {
    position: absolute; left: 0; width: 100%;
    font-family: "Cinzel", serif; font-weight: 400; line-height: 1;
  }
  .back-title.line-one { top: 48px; font-size: 70px; letter-spacing: 0.02em; }
  .back-title.line-two { top: 126px; font-size: 66px; letter-spacing: 0.02em; }
  .service-list {
    position: absolute; top: 200px; left: 0; width: 100%;
    font-family: "Cinzel", serif; font-weight: 500;
    font-size: 19px; line-height: 21px; letter-spacing: 0.02em;
  }
</style>
</head>
<body>
<main class="canvas">
  <section class="card card-front" aria-label="Business card front">
    <div class="brand-name">MERIDALE</div>
    <div class="brand-sub"><span class="rule"></span><span class="word">PAINTING</span><span class="rule"></span></div>
    <div class="holder-name">Tobin Hale</div>
    <div class="holder-role">Managing Director</div>
    <div class="holder-divider"></div>
    <ul class="contact-list">
      <li>P: 055-201 384 617</li>
      <li>M: 055-201 384 617</li>
      <li>E: hello@meridalemail.com</li>
    </ul>
  </section>

  <section class="card card-back" aria-label="Business card back">
    <div class="paint-field" role="img" aria-label="Textured abstract acrylic paint strokes in red, orange, gold, blue and magenta"></div>
    <div class="back-title line-one">Meridale</div>
    <div class="back-title line-two">PAINTING</div>
    <p class="service-list">
      We paint residential and commercial,<br>
      interior&amp; exterior painting, cabinets<br>
      refinish,acoustic ceiling painting,popcorn<br>
      ceiling removal,drywall repair,iron<br>
      and concrete painting
    </p>
  </section>
</main>
</body>
</html>
```